Advertising campaign - Red Tape Reduction

We are doing an advertising campaign about reducing Red Tape (this is a term used to mean administrative slowing down of a process. We want to produce an image that has a picture of a roll of red tape.... being wound up, and instead a red Carpet is being rolled out.<br/>The slogan would be <br/>"Roll Out the Red Carpet and Roll up the Red Tape"

Target Market(s)

1 -Business Owners,
2- Government decision makers,
3 - General Public

Logo Text

"Roll out the Red Carpet and Roll up the Red Tape"

Font styles to use
Serif
Sans Serif

Colors

Designer to choose colors to be used in the design.

Requirements
Must have
• This project mist have red carpet being rolled out, and red tape being rolled up.... the image should explain everything
• It must have the slogan "Roll Out the Red Carpet and Roll up the Red Tape"

```html
<!DOCTYPE html>
<html lang="en">
<head>
<meta charset="utf-8">
<title>Roll Out the Red Carpet and Roll up the Red Tape</title>
<link href="https://fonts.googleapis.com/css2?family=Montserrat:wght@600&family=Questrial&display=swap" rel="stylesheet">
<style>
  :root {
    --red: #e3141e;
    --navy: #0f2a3d;
    --ink: #1c1c1c;
    --paper: #ffffff;
    --mist-light: #f2f5f8;
    --mist-mid: #c9d3dc;
    --mist-dark: #8d9aa6;
  }
  * { margin: 0; padding: 0; box-sizing: border-box; }
  html, body { width: 927px; height: 1200px; overflow: hidden; background: var(--paper); }
  .page { position: relative; width: 927px; height: 1200px; overflow: hidden; background: var(--paper); }

  .hero {
    position: absolute; left: 0; top: 0; width: 927px; height: 391px;
    background:
      radial-gradient(ellipse at 30% 95%, #9e1a1a 0%, rgba(158,26,26,0.75) 10%, rgba(158,26,26,0) 24%),
      radial-gradient(ellipse at 50% 115%, var(--mist-light) 0%, var(--mist-mid) 45%, rgba(201,211,220,0) 70%),
      radial-gradient(circle at 70% 15%, #ffffff 0%, var(--mist-light) 30%, var(--mist-mid) 65%, var(--mist-dark) 100%);
  }
  .headline {
    position: absolute; right: 62px; top: 58px;
    font-family: "Montserrat", sans-serif; font-weight: 600;
    font-size: 46px; line-height: 68px; color: var(--red);
    text-align: right; letter-spacing: 0.3px;
  }
  .hero-band { position: absolute; left: 0; top: 391px; width: 927px; height: 15px; background: var(--navy); }

  .column {
    position: absolute; top: 452px;
    font-family: "Questrial", sans-serif; font-size: 14px; line-height: 25px;
    letter-spacing: 1.6px; color: var(--ink); text-align: justify; hyphens: auto;
  }
  .column-left { left: 91px; width: 341px; }
  .column-right { left: 501px; width: 335px; }

  .brand {
    position: absolute; left: 501px; top: 1090px; width: 335px; height: 30px;
    display: flex; align-items: center; justify-content: flex-end; gap: 12px;
  }
  .brand-square { width: 18px; height: 18px; background: var(--red); flex: none; }
  .brand-name {
    font-family: "Questrial", sans-serif; font-size: 20px;
    color: var(--navy); letter-spacing: 0.2px; white-space: nowrap;
  }
</style>
</head>
<body>
<main class="page">
  <section class="hero" role="img" aria-label="A roll of red tape winding up at the top left while a red carpet unrolls toward the viewer between rope barriers on a misty white stage"></section>
  <h1 class="headline">Roll Out the<br>Red Carpet and<br>Roll up the<br>Red Tape</h1>
  <div class="hero-band"></div>

  <article class="column column-left">
    <p>Lorem ipsum dolor sit amet, consectetur adipiscing elit, sed do eiusmod tempor incididunt ut labore et dolore magna aliqua. Condimentum mattis pellentesque id nibh tortor. Interdum posuere lorem ipsum dolor sit amet consectetur adipiscing. Viverra accumsan in nisl nisi. At consectetur lorem donec massa sapien. Aenean vel elit scelerisque mauris pellentesque pulvinar. Et tortor at risus viverra. Amet consectetur adipiscing elit duis. Erat imperdiet sed euismod nisi. Mauris augue neque gravida in fermentum et. Et malesuada fames ac turpis.</p>
    <p>Adipiscing commodo elit at imperdiet dui accumsan sit. Lacus sed turpis tincidunt id aliquet risus feugiat in. Sociis natoque penatibus et magnis dis parturient montes. Faucibus scelerisque eleifend donec pretium vulputate sapien nec. Et sollicitudin ac orci phasellus egestas tellus rutrum tellus. Urna neque viverra justo nec ultrices. Nascetur ridiculus mus mauris vitae. Tempus quam pellentesque nec nam aliquam. Magna ac placerat vestibulum lectus. Fermentum odio eu feugiat pretium nibh ipsum consequat. Ac feugiat</p>
  </article>

  <article class="column column-right">
    <p>Tincidunt arcu non sodales neque sodales. Magna sit amet purus gravida quis blandit turpis cursus in. Et pharetra pharetra massa massa ultricies mi quis hendrerit dolor. Porta lorem mollis aliquam ut porttitor. In est ante in nibh. A scelerisque purus semper eget duis at. Auctor eu augue ut lectus arcu bibendum at. Condimentum id venenatis a condimentum vitae sapien pellentesque.</p>
    <p>Nec nam aliquam sem et tortor consequat id porta. Fermentum iaculis eu non diam phasellus. Ut tristique et egestas quis ipsum suspendisse. Sed vulputate odio ut enim blandit volutpat maecenas volutpat blandit. Etiam erat velit scelerisque in dictum non. Quis commodo odio aenean sed adipiscing diam. Sem nulla pharetra diam sit amet nisl suscipit adipiscing. Vitae et leo duis ut diam quam. Justo laoreet sit amet cursus sit amet dictum. Faucibus nisl tincidunt eget nullam non nisi. Massa eget egestas purus viverra.</p>
  </article>

  <footer class="brand">
    <span class="brand-square"></span>
    <span class="brand-name">Harbourline Business Council</span>
  </footer>
</main>
</body>
</html>
```